Harrowden Metal recycling, a business card/logo for our industrial family metal recycling company

A new business card design/logo for our long established family metal recycling company.
I have a logo for our property company which was designed a few months ago on pixel forge which I would like to be very close to this design but have a more industrial feel to it and in a darker blue colour, please see attachments.

Target Market(s)

industries that produce metal waste for recycling, construction sites, engineering companies, manufactures, builders, plumbers, electricians, general house holders.

Industry/Entity Type

Recycling

Contact Information for Business Card

owner/director...Martin harrowden
e-mail....info@harrowdenscrapworks.co.uk
web address.....harrowdenscrapworks.co.uk

Font styles to use
Serif
Sans Serif

Colors
0255a3
ffffff

Requirements
Must have
• -dark blue business card on front.
-white on the back, see contact details, e-mail address for metal company.
-to have an industrial feel to it.
-harrowden logo as business card attached but (harrowden metal recycling)
please remove the little roof/arrow above harrowden as this was relevant to property company.
Nice to have
• please see our website harrowdenscrapworks.co.uk with all details
being correct however I would like to refresh the logo to more like the harrowden property investment business card logo attached.
Should not have
• should not contain details from property investments card as this design is for the metal recycling company.

```html
<!DOCTYPE html>
<html lang="en">
<head>
<meta charset="utf-8">
<title>Harrowden Metal Recycling – Business Card</title>
<link rel="stylesheet" href="https://fonts.googleapis.com/css2?family=Open+Sans:wght@400;600;700&display=swap">
<style>
  :root {
    --backdrop: #3b3431;
    --card-white: #f7f7f8;
    --card-black: #111111;
    --brand-blue: #2b3990;
    --ink-grey: #3a3a3a;
    --rule-grey: #9a9a9a;
    --silver: #d9dadc;
  }
  * { box-sizing: border-box; margin: 0; padding: 0; }
  html, body { width: 1200px; height: 844px; overflow: hidden; }
  body {
    background: var(--backdrop);
    font-family: "Open Sans", Arial, sans-serif;
    position: relative;
  }
  .card {
    position: absolute;
    top: 263px;
    width: 520px;
    height: 318px;
    border-radius: 3px;
    box-shadow: 0 10px 24px rgba(0,0,0,.45);
  }
  .card--front { left: 60px; background: var(--card-white); }
  .card--back  { left: 620px; background: var(--card-black); }

  .brand {
    position: absolute;
    left: 0; right: 0;
    display: flex;
    align-items: center;
    justify-content: center;
    gap: 12px;
  }
  .brand__mark {
    width: 26px; height: 26px;
    border-radius: 50%;
    border: 3px solid currentColor;
  }
  .brand__name {
    font-weight: 600;
    font-size: 27px;
    letter-spacing: .5px;
  }
  .card--front .brand { top: 78px; color: var(--brand-blue); }
  .card--back  .brand { top: 130px; color: var(--silver); }

  .holder {
    position: absolute;
    right: 330px;
    top: 222px;
    text-align: right;
  }
  .holder__name {
    color: var(--brand-blue);
    font-weight: 700;
    font-size: 16px;
    letter-spacing: .2px;
  }
  .holder__role {
    color: var(--ink-grey);
    font-size: 12px;
    margin-top: 1px;
  }
  .divider {
    position: absolute;
    left: 205px;
    top: 190px;
    width: 1px;
    height: 78px;
    background: var(--rule-grey);
  }
  .contacts {
    position: absolute;
    left: 220px;
    top: 188px;
    list-style: none;
    font-size: 13px;
    color: var(--ink-grey);
    line-height: 21px;
  }
  .contacts li { display: flex; align-items: center; gap: 5px; }
  .contacts svg { width: 13px; height: 13px; fill: var(--brand-blue); flex: none; }
  .contacts .web { color: var(--brand-blue); }
</style>
</head>
<body>

<section class="card card--front" aria-label="Business card, contact side">
  <div class="brand">
    <span class="brand__mark"></span>
    <span class="brand__name">Harrowden Metal Recycling</span>
  </div>

  <div class="holder">
    <p class="holder__name">MARTIN HARROWDEN</p>
    <p class="holder__role">Owner-Director</p>
  </div>

  <span class="divider"></span>

  <ul class="contacts">
    <li>
      <svg viewBox="0 0 16 16" aria-hidden="true"><path d="M1 6c0-2 3-4 7-4s7 2 7 4v1h-4V5.5C10 5 9 5 8 5s-2 0-3 .5V7H1z M3 8h10l1 6H2z"/></svg>
      07700 900418
      <svg viewBox="0 0 16 16" aria-hidden="true"><path d="M4 1h8v14H4z M5.5 3v9h5V3z"/></svg>
      020 7946 0731
    </li>
    <li>
      <svg viewBox="0 0 16 16" aria-hidden="true"><path d="M1 3h14v10H1z M2 4.5v.5l6 4 6-4v-.5z" fill-rule="evenodd"/></svg>
      info@harrowdenmetalrecycling.co.uk
    </li>
    <li>
      <svg viewBox="0 0 16 16" aria-hidden="true"><circle cx="8" cy="8" r="7"/></svg>
      <span>www.<span class="web">harrowdenmetalrecycling</span>.co.uk</span>
    </li>
  </ul>
</section>

<section class="card card--back" aria-label="Business card, brand side">
  <div class="brand">
    <span class="brand__mark"></span>
    <span class="brand__name">Harrowden Metal Recycling</span>
  </div>
</section>

</body>
</html>
```